Brightvale Inc. Business Card Design

Brightvale Inc. is in search of a great clean design for our business cards!

Looking to incorporate our full logo and watermark on side one (however, I am open to having the text and watermark separated within the design.)

On side two, I am looking to have contact information (Name, Position, Phone #, Email, Website (www.thebrightvale.ca). Can have the logo and/or watermark as part of the design if applicable.

Please add tagline "Where Shine Counts" on either side 1 or 2. This tagline can be in a sans serif, serif or cursive font as long as it compliments overall design. Capitalization can be title or sentence case depending on how it fits within the design.

Get creative!! Looking for a clean, crisp, premium design! Looking for a glossy card finish with spot UV features when printed. Cards will also be printed with rounded corners. Standard dimensions (3.5 x 2).

Target Market(s)

B2B - primary clients are business owners or property management corporations. (residential jobs are few and far between)

Industry/Entity Type

Business

Contact Information for Business Card

- clean, crisp design
- double sided
- spot UV accents and glossy finish upon printing
- standard business card size (3.5 x 2) with rounded corners
- please see project description for requirements per side

Font styles to use
Sans Serif

Requirements
Must have
• - adequate bleeds with print ready files
• - cohesive design elements between side 1 & 2
• - spot UV elements (can be on both sides or just one, use your discretion)
• - colour pallet should match the logo file provided
• - incorporate tagline "where shine counts" (this tagline can be in a serif or sans serif font as long as it is complimentary to the overall design.
Nice to have
• - Premium elements with a clean design
Should not have
• - Please omit cartoon or whimsical like designs, think premium.
• - Colours should not stray from the pallet of the provided logo.

```html
<!DOCTYPE html>
<html lang="en">
<head>
<meta charset="utf-8">
<title>Brightvale Inc. Business Card</title>
<link href="https://fonts.googleapis.com/css2?family=Montserrat:wght@500&family=Roboto:wght@400;500;700&display=swap" rel="stylesheet">
<style>
  :root {
    --teal: #14999a;
    --navy: #1c1e47;
    --ink: #2a2a33;
    --stage: #e4e4e4;
    --card-top: #f1f1f1;
    --card-bottom: #e2e2e2;
  }
  * { margin: 0; padding: 0; box-sizing: border-box; }
  html, body {
    width: 1200px; height: 576px; overflow: hidden;
    background: var(--stage);
    font-family: "Roboto", Arial, sans-serif;
  }
  .canvas { position: relative; width: 1200px; height: 576px; }
  .card {
    position: absolute; top: 139px;
    width: 484px; height: 293px;
    border-radius: 14px; overflow: hidden;
    background: linear-gradient(160deg, var(--card-top), var(--card-bottom));
    box-shadow: 0 2px 5px rgba(0,0,0,0.18);
  }
  .card--front { left: 82px; }
  .card--back { left: 602px; }

  .front-brand {
    position: absolute; left: 0; right: 0; top: 118px;
    display: flex; align-items: center; justify-content: center; gap: 14px;
  }
  .brand-mark { width: 44px; height: 44px; background: var(--teal); }
  .brand-name {
    font-weight: 700; color: var(--teal); letter-spacing: -0.5px; line-height: 1;
  }
  .front-brand .brand-name { font-size: 46px; }

  .back-brand {
    position: absolute; left: 28px; top: 82px; width: 230px;
    display: flex; flex-direction: column; align-items: center; gap: 22px;
  }
  .back-brand .brand-mark { width: 54px; height: 54px; }
  .back-brand .brand-name { font-size: 30px; }

  .contact { position: absolute; left: 282px; top: 56px; color: var(--ink); }
  .contact-name { font-size: 22px; font-weight: 500; color: var(--teal); }
  .contact-role { font-size: 12px; margin-top: 3px; }
  .contact-address { font-size: 12.5px; line-height: 17px; margin-top: 22px; }
  .contact-lines { list-style: none; margin-top: 4px; font-size: 12.5px; }
  .contact-lines li { display: flex; align-items: center; gap: 10px; height: 18px; }
  .contact-lines svg { width: 11px; height: 11px; fill: var(--teal); flex: none; }
  .accent { color: var(--teal); }

  .footer-band { position: absolute; left: 0; bottom: 0; width: 484px; height: 36px; }
  .tagline {
    position: absolute; right: 36px; bottom: 8px;
    font-family: "Montserrat", Arial, sans-serif; font-size: 11.5px;
    color: #fff; letter-spacing: 0.6px;
  }
</style>
</head>
<body>
<main class="canvas">
  <section class="card card--front" aria-label="Card front">
    <div class="front-brand">
      <span class="brand-mark"></span>
      <span class="brand-name">Brightvale Inc.</span>
    </div>
  </section>

  <section class="card card--back" aria-label="Card back">
    <div class="back-brand">
      <span class="brand-mark"></span>
      <span class="brand-name">Brightvale Inc.</span>
    </div>

    <div class="contact">
      <p class="contact-name">Daniel Reyes</p>
      <p class="contact-role">Managing Director</p>
      <p class="contact-address">48 Harbour Lane<br>Suite 9, Canada</p>
      <ul class="contact-lines">
        <li><svg viewBox="0 0 12 12"><path d="M1 4c0-2 2-3 5-3s5 1 5 3l-2 1-1-2H4L3 5zM3 6h6l2 5H1z"/></svg>1800-555-0142</li>
        <li><svg viewBox="0 0 12 12"><path d="M1 2h10v8H1zM2 3l4 3 4-3v1L6 7 2 4z" fill-rule="evenodd"/></svg>dreyes@brightvale.ca</li>
        <li><svg viewBox="0 0 12 12"><circle cx="6" cy="6" r="5"/></svg>www.<span class="accent">thebrightvale</span>.ca</li>
      </ul>
    </div>

    <svg class="footer-band" viewBox="0 0 484 36" preserveAspectRatio="none" aria-hidden="true">
      <rect x="0" y="20" width="260" height="16" fill="var(--navy)"/>
      <polygon points="258,0 484,0 484,36 240,36" fill="var(--teal)"/>
    </svg>
    <p class="tagline">Where Shine Counts</p>
  </section>
</main>
</body>
</html>
```